Design business card for new business which advocates for elders in nursing homes or personal care h

New business for rights of the elderly residents who reside in personal care homes and or nursing homes. I am looking for a business card with logo of keystone for Pennsylvania and something in side the keystone that represents healthcare, advocates, something on that line; monitor care received and needs of resident. Chart audits, State Regulation compliance

Target Market(s)

Seniors no longer safe to live at home by themselves along with their kids

Industry/Entity Type

Business

Contact Information for Business Card

Keystone symbol to represent Pensylvaoa with some kind of symbol inside to represent advocate, seniors, or healthcare symbol

Font styles to use
Serif

Colors
33a6d7
85cae6
abd037

Requirements
Must have
• Brightwell Elder Allies is our business name; our tag line is Path to Better Living
Nice to have
• Nice logo

```html
<!DOCTYPE html>
<html lang="en">
<head>
<meta charset="utf-8">
<title>Brightwell Elder Allies — Business Card Concepts</title>
<link href="https://fonts.googleapis.com/css2?family=EB+Garamond:wght@400;500&display=swap" rel="stylesheet">
<style>
  :root {
    --frame-blue: #2a82c6;
    --name-blue: #1f7bc1;
    --sky: #29a9dc;
    --teal: #5bc4d0;
    --teal-line: #9fdbe2;
    --soft-blue: #8fbfe2;
    --ink: #666666;
    --tag-grey: #7a7a7a;
    --grey-bar: #777777;
    --green-bar: #0f9a2b;
    --paper: #ffffff;
  }
  * { margin: 0; padding: 0; box-sizing: border-box; }
  html, body { width: 1200px; height: 1000px; overflow: hidden; background: var(--paper); }
  body { position: relative; font-family: "EB Garamond", Georgia, serif; color: var(--ink); }

  .card { position: absolute; top: 143px; width: 274px; height: 515px; }
  .card-front { border: 6px solid var(--frame-blue); background: var(--paper); }
  .card-back { border: 1px solid var(--teal-line); background: var(--paper); overflow: hidden; }
  .back-band { position: absolute; left: 0; top: 0; right: 0; height: 258px; background: var(--teal); }
  .back-mark { position: absolute; right: -70px; bottom: -60px; width: 240px; height: 240px; }

  .accent-bar { position: absolute; left: -6px; bottom: -6px; width: 137px; height: 6px; }
  .accent-grey { background: var(--grey-bar); }
  .accent-green { background: var(--green-bar); }

  .brand { position: absolute; left: 16px; top: 68px; display: flex; align-items: center; gap: 7px; }
  .brand-dot { width: 18px; height: 18px; border-radius: 50%; background: var(--name-blue); flex: none; }
  .brand-words { display: flex; flex-direction: column; align-items: flex-end; }
  .brand-name { font-size: 21px; font-weight: 500; color: var(--name-blue); white-space: nowrap; line-height: 1; }
  .brand-tagline { font-size: 11px; color: var(--tag-grey); text-transform: uppercase; letter-spacing: 0.6px; white-space: nowrap; line-height: 1; margin-top: 4px; }

  .person { position: absolute; left: 13px; top: 352px; }
  .person-name { font-size: 20px; color: var(--sky); line-height: 1; letter-spacing: 0.3px; }
  .person-role { font-size: 15px; color: var(--ink); line-height: 1.2; margin-top: 2px; }

  .contact { position: absolute; left: 13px; list-style: none; font-size: 14px; line-height: 18px; color: var(--ink); }
  .contact li { display: flex; align-items: center; gap: 6px; }
  .contact-direct { top: 408px; }
  .contact-online { top: 457px; }
  .icon { width: 14px; height: 14px; flex: none; display: block; }

  .lockup { position: absolute; top: 850px; display: flex; align-items: center; gap: 14px; }
  .lockup .brand-dot { width: 46px; height: 46px; }
  .lockup .brand-name { font-size: 50px; }
  .lockup .brand-tagline { font-size: 22px; letter-spacing: 1px; margin-top: 2px; }
</style>
</head>
<body>

  <!-- Concept A -->
  <section class="card card-front" style="left:28px;">
    <div class="brand">
      <span class="brand-dot"></span>
      <div class="brand-words"><span class="brand-name">Brightwell Elder Allies</span><span class="brand-tagline">Path to Better Living</span></div>
    </div>
    <div class="person">
      <p class="person-name">YOUR NAME</p>
      <p class="person-role">Designation</p>
    </div>
    <ul class="contact contact-direct">
      <li><svg class="icon" viewBox="0 0 14 14"><rect width="14" height="14" rx="2" fill="#29a9dc"/><rect x="4.5" y="2.5" width="5" height="9" rx="1" fill="none" stroke="#fff" stroke-width="1.2"/></svg>000-000-0000</li>
      <li><svg class="icon" viewBox="0 0 14 14"><rect width="14" height="14" rx="2" fill="#29a9dc"/><rect x="2.5" y="4" width="9" height="6" fill="none" stroke="#fff" stroke-width="1.1"/><path d="M2.5 4 7 7.5 11.5 4" fill="none" stroke="#fff" stroke-width="1.1"/></svg>yourname@brightwellallies.com</li>
    </ul>
    <ul class="contact contact-online">
      <li><svg class="icon" viewBox="0 0 14 14"><rect width="14" height="14" rx="2" fill="#29a9dc"/><circle cx="7" cy="7" r="4.3" fill="none" stroke="#fff" stroke-width="1.1"/><path d="M2.7 7h8.6M7 2.7v8.6" stroke="#fff" stroke-width="1"/></svg>www.brightwellallies.com</li>
      <li><svg class="icon" viewBox="0 0 14 14"><rect width="14" height="14" rx="2" fill="#1f5f9e"/></svg>social: /brightwellallies</li>
    </ul>
    <span class="accent-bar accent-grey"></span>
  </section>

  <section class="card card-back" style="left:307px;">
    <div class="back-band"></div>
    <svg class="back-mark" viewBox="0 0 240 240" role="img" aria-label="Large faded brand mark area"><circle cx="120" cy="120" r="120" fill="#8fbfe2" opacity="0.7"/></svg>
  </section>

  <!-- Concept B -->
  <section class="card card-front" style="left:619px;">
    <div class="brand">
      <span class="brand-dot"></span>
      <div class="brand-words"><span class="brand-name">Brightwell Elder Allies</span><span class="brand-tagline">Path to Better Living</span></div>
    </div>
    <div class="person">
      <p class="person-name">YOUR NAME</p>
      <p class="person-role">Designation</p>
    </div>
    <ul class="contact contact-direct">
      <li><svg class="icon" viewBox="0 0 14 14"><rect width="14" height="14" rx="2" fill="#29a9dc"/><rect x="4.5" y="2.5" width="5" height="9" rx="1" fill="none" stroke="#fff" stroke-width="1.2"/></svg>000-000-0000</li>
      <li><svg class="icon" viewBox="0 0 14 14"><rect width="14" height="14" rx="2" fill="#29a9dc"/><rect x="2.5" y="4" width="9" height="6" fill="none" stroke="#fff" stroke-width="1.1"/><path d="M2.5 4 7 7.5 11.5 4" fill="none" stroke="#fff" stroke-width="1.1"/></svg>yourname@brightwellallies.com</li>
    </ul>
    <ul class="contact contact-online">
      <li><svg class="icon" viewBox="0 0 14 14"><rect width="14" height="14" rx="2" fill="#29a9dc"/><circle cx="7" cy="7" r="4.3" fill="none" stroke="#fff" stroke-width="1.1"/><path d="M2.7 7h8.6M7 2.7v8.6" stroke="#fff" stroke-width="1"/></svg>www.brightwellallies.com</li>
      <li><svg class="icon" viewBox="0 0 14 14"><rect width="14" height="14" rx="2" fill="#1f5f9e"/></svg>social: /brightwellallies</li>
    </ul>
    <span class="accent-bar accent-green"></span>
  </section>

  <section class="card card-back" style="left:898px;">
    <div class="back-band"></div>
    <svg class="back-mark" viewBox="0 0 240 240" role="img" aria-label="Large faded brand mark area"><circle cx="120" cy="120" r="120" fill="#8fbfe2" opacity="0.7"/></svg>
  </section>

  <!-- Logo lockups -->
  <div class="lockup" style="left:100px;">
    <span class="brand-dot"></span>
    <div class="brand-words"><span class="brand-name">Brightwell Elder Allies</span><span class="brand-tagline">Path to Better Living</span></div>
  </div>
  <div class="lockup" style="left:645px;">
    <span class="brand-dot"></span>
    <div class="brand-words"><span class="brand-name" style="font-size:46px;">Brightwell Elder Allies</span><span class="brand-tagline">Path to Better Living</span></div>
  </div>

</body>
</html>
```